Stationery for consulting company
Strategic Thinking. Inclusive Solutions. Measurable Impact
Project: Stationery for consulting company
Business Cards and Stationery
Professional
Benedo Ofurame Phd
Senior Partner
Plot 9 Umoru Close Oregun, Ikeja Lagos - Nigeria
Benedo.ofura@velmarq.com
www.velmarq.com
fdsfdffdsd

```html
<!DOCTYPE html>
<html lang="en">
<head>
<meta charset="utf-8">
<title>Velmarq – Business Card</title>
<link rel="stylesheet" href="https://fonts.googleapis.com/css2?family=Montserrat:wght@400;500;700;800&display=swap">
<style>
  :root {
    --bg: #e6e7e8;
    --green: #0f5a37;
    --green-dark: #0a4028;
    --green-light: #1f7a50;
    --orange: #e0651e;
    --white: #ffffff;
    --grey: #6d6e70;
    --text: #3a3b3d;
  }
  * { margin: 0; padding: 0; box-sizing: border-box; }
  html, body {
    width: 1200px; height: 901px; overflow: hidden;
    background: var(--bg);
    font-family: "Montserrat", Arial, sans-serif;
  }
  .stage { position: relative; width: 1200px; height: 901px; }
  .card {
    position: absolute; left: 300px; width: 600px; height: 350px;
    border-radius: 22px; overflow: hidden;
    box-shadow: 0 14px 30px rgba(0,0,0,0.18);
  }
  .card-back { top: 70px; }
  .card-back .pattern {
    width: 100%; height: 100%;
    background: linear-gradient(120deg, var(--green-dark) 0%, var(--green) 45%, var(--green-light) 70%, var(--green-dark) 100%);
  }
  .card-front { top: 470px; background: var(--white); }
  .brand {
    position: absolute; top: 28px; right: 32px;
    display: flex; align-items: center; gap: 10px;
  }
  .brand-dot { width: 36px; height: 36px; border-radius: 50%; background: var(--green); }
  .brand-name { font-weight: 800; font-size: 30px; color: var(--green); letter-spacing: 2px; }
  .person { position: absolute; left: 32px; top: 168px; }
  .person-name { font-weight: 800; font-size: 24px; color: var(--green); letter-spacing: 0.5px; }
  .person-name .title { color: var(--orange); }
  .person-role { font-size: 13px; color: var(--grey); margin-top: 2px; }
  .contacts, .address {
    position: absolute; top: 248px;
    font-size: 12.5px; color: var(--text); line-height: 19px;
  }
  .contacts { left: 32px; }
  .contacts li { list-style: none; display: flex; align-items: center; gap: 8px; }
  .contacts svg { width: 11px; height: 11px; fill: var(--green); }
  .address { right: 32px; text-align: right; font-style: normal; }
  .wave { position: absolute; left: 0; top: 0; width: 600px; height: 350px; }
  .website { position: absolute; right: 32px; bottom: 12px; font-size: 12.5px; color: var(--white); }
</style>
</head>
<body>
<main class="stage">
  <section class="card card-back">
    <div class="pattern" role="img" aria-label="Dark green card back with a repeating tonal brand-symbol pattern and soft sheen"></div>
  </section>

  <section class="card card-front">
    <div class="brand">
      <span class="brand-dot"></span>
      <span class="brand-name">VELMARQ</span>
    </div>

    <div class="person">
      <h1 class="person-name">BENEDO OFURAME <span class="title">PHD</span></h1>
      <p class="person-role">Senior Partner</p>
    </div>

    <ul class="contacts">
      <li><svg viewBox="0 0 24 24"><path d="M6.6 10.8a15.1 15.1 0 0 0 6.6 6.6l2.2-2.2a1 1 0 0 1 1-.25 11.4 11.4 0 0 0 3.6.57 1 1 0 0 1 1 1V20a1 1 0 0 1-1 1A17 17 0 0 1 3 4a1 1 0 0 1 1-1h3.5a1 1 0 0 1 1 1c0 1.250.2 2.450.57 3.57a1 1 0 0 1-.25 1z"/></svg>+234 (0) 805 611 4870</li>
      <li><svg viewBox="0 0 24 24"><path d="M2 5h20v14H2zm2 2v.5l8 5 8-5V7l-8 5z"/></svg>Benedo.ofura@velmarq.com</li>
    </ul>

    <address class="address">
      Plot 9 Umoru Close Oregun<br>Ikeja Lagos - Nigeria
    </address>

    <svg class="wave" viewBox="0 0 600 350" aria-hidden="true">
      <path d="M0 306 C130 300 280 318 600 297 L600 301 C300 326 140 314 0 318 Z" fill="var(--orange)"/>
      <path d="M0 326 C170 314 370 330 600 302 L600 350 L0 350 Z" fill="var(--green)"/>
    </svg>
    <span class="website">www.velmarq.com</span>
  </section>
</main>
</body>
</html>
```